Recruitment technology firm needs a downloadable pdf to generate leads.

We need design work for a downloadable pdf that will serve as an educational document to visitors to our website. We help clients identify candidates that fit their job posting. We do that by defining the personality of the job and then assessing the personality of the candidates. We then mathematically compare and rank all the candidates against the job. Our colour scheme is blue. The final design should move from communicating a lack of fit or frustration to people fitting their job and success per the text we have built. People who download this lead generator will be added to our email list for re-marketing purposes. our website is www.tallowridgeadvisory.com. I've attached an example of a lead generator (ebike)for a business unrelated to ours.

Target Market(s)

Our target market is businesses of 50-300 people, we're targeting business owners or executives of entrepreneurial (vs. corporate) companies.

Colors
85acd3
3377b5
0455a3

Requirements
Must have
• Easy to read so text isn't overwhelming.
Nice to have
• Don't be compelled to use our website photos or those like it. I'd like this to reflect entrepreneurial companies, not corporate, suit and tie companies.

```html
<!DOCTYPE html>
<html lang="en">
<head>
<meta charset="utf-8">
<title>Tools and Services for the Growth Mindset – Tallowridge</title>
<link href="https://fonts.googleapis.com/css2?family=Montserrat:wght@300;400;500;600;700;800&display=swap" rel="stylesheet">
<style>
  :root {
    --ink: #1d1d1f;
    --sky: #29a8da;
    --ocean: #16709f;
    --ocean-text: #0e6aa0;
    --paper: #ffffff;
    --backdrop: #ffffff;
    --body-grey: #3a3a3a;
  }
  * { margin: 0; padding: 0; box-sizing: border-box; }
  html, body { width: 1200px; height: 2812px; overflow: hidden; background: var(--backdrop); }
  body { position: relative; font-family: 'Montserrat', sans-serif; color: var(--ink); }

  .page {
    position: absolute; left: 175px; width: 851px; height: 1204px;
    background: var(--paper);
    box-shadow: 0 6px 18px rgba(0,0,0,0.14);
  }
  .page--cover { top: 118px; }
  .page--article { top: 1435px; }

  /* Cover */
  .cover-block { position: absolute; left: 72px; top: 0; width: 225px; height: 297px; background: var(--sky); }
  .cover-title { position: absolute; left: 117px; top: 96px; font-size: 51px; line-height: 59px; font-weight: 400; letter-spacing: 0.5px; white-space: nowrap; }
  .cover-title strong { font-weight: 800; display: block; }
  .cover-photo {
    position: absolute; left: 0; top: 345px; width: 851px; height: 650px;
    background: linear-gradient(180deg, #e9edf0 0%, #c9d0d6 35%, #5c6670 62%, #2a3038 80%, #8b9299 100%);
  }
  .brand { position: absolute; display: flex; align-items: center; gap: 12px; font-weight: 700; color: var(--ink); white-space: nowrap; }
  .brand-dot { background: var(--ocean); border-radius: 50%; flex: none; }
  .cover-brand { left: 72px; top: 1082px; font-size: 40px; }
  .cover-brand .brand-dot { width: 38px; height: 38px; }
  .site { position: absolute; font-size: 19px; font-weight: 400; color: var(--ink); white-space: nowrap; }
  .cover-site { left: 512px; top: 1100px; }

  /* Article */
  .hero-band {
    position: absolute; left: 44px; top: 55px; width: 753px; height: 330px;
    background: var(--ocean); color: #fff; padding: 34px 33px 0;
  }
  .hero-title { font-size: 45px; line-height: 57px; font-weight: 700; letter-spacing: 0.5px; }
  .hero-title span { display: block; font-weight: 400; }
  .hero-rule { width: 105px; height: 3px; background: #fff; margin: 16px 0 20px; }
  .hero-lead { font-size: 22px; line-height: 27px; font-weight: 500; }
  .hero-body { font-size: 14px; line-height: 17px; font-weight: 400; margin-top: 20px; width: 660px; }

  .intro { position: absolute; left: 75px; top: 405px; font-size: 19px; line-height: 26px; font-weight: 600; width: 600px; }

  .reason { position: absolute; height: 200px; }
  .reason-badge {
    position: absolute; left: 0; top: 0; width: 54px; height: 54px; border-radius: 50%;
    border: 3px solid var(--ocean-text); display: flex; align-items: center; justify-content: center;
    font-size: 24px; font-weight: 700; color: var(--ink);
    box-shadow: 0 0 0 3px #fff, 0 0 0 4px #9fb7c8;
  }
  .reason-heading { position: absolute; left: 77px; top: 0; font-size: 17.5px; line-height: 21px; font-weight: 600; color: var(--ocean-text); white-space: nowrap; }
  .reason-text { position: absolute; left: 77px; font-size: 11.2px; line-height: 13.8px; color: var(--body-grey); text-align: justify; hyphens: auto; }

  .reason--1 { left: 75px; top: 491px; width: 310px; }
  .reason--2 { left: 454px; top: 491px; width: 340px; }
  .reason--3 { left: 75px; top: 720px; width: 310px; }
  .reason--4 { left: 454px; top: 720px; width: 340px; }
  .reason--5 { left: 75px; top: 968px; width: 720px; height: 100px; }
  .reason--1 .reason-text, .reason--3 .reason-text { width: 227px; }
  .reason--2 .reason-text, .reason--4 .reason-text { width: 250px; }
  .reason--5 .reason-text { width: 637px; top: 30px; }
  .reason--1 .reason-text, .reason--2 .reason-text { top: 68px; }
  .reason--3 .reason-text, .reason--4 .reason-text { top: 74px; }

  .article-brand { left: 46px; top: 1100px; font-size: 28px; gap: 8px; }
  .article-brand .brand-dot { width: 28px; height: 28px; }
  .article-site { left: 523px; top: 1104px; }
</style>
</head>
<body>

<section class="page page--cover">
  <div class="cover-block"></div>
  <h1 class="cover-title">TOOLS AND<br>SERVICES FOR<strong>THE GROWTH MINDSET</strong></h1>
  <div class="cover-photo" role="img" aria-label="Photo of a team meeting around a conference table in a bright office"></div>
  <div class="brand cover-brand"><span class="brand-dot"></span>TALLOWRIDGE</div>
  <div class="site cover-site">www.tallowridgeadvisory.com</div>
</section>

<section class="page page--article">
  <div class="hero-band">
    <h2 class="hero-title">5 REASONS YOU SUCK<span>AT HIRING FOR FIT</span></h2>
    <div class="hero-rule"></div>
    <p class="hero-lead">Hiring the wrong fit is painful, we are with you there.<br>Bad hires ruin your day, every day..</p>
    <p class="hero-body">You want to make sure your next hire is the right one. You know what it’s like when you hire the wrong person – they aren’t productive, they don’t get along with others, there’s tension, you have to let them go, and you re-start the whole process over again.</p>
  </div>

  <p class="intro">Our goal is to help you stop this cycle. Here are 5 mistakes you are likely making.</p>

  <div class="reason reason--1">
    <div class="reason-badge">1</div>
    <h3 class="reason-heading">You have not defined the<br>obstacles found in the job</h3>
    <p class="reason-text">a. Every job has its challenges and you need to find someone who will deal with the challenges as a high performer would. Spending too much time in unstructured conversation or putting too much emphasis on selling the role can detract from this key insight. Define the top 2-5 obstacles and learn how the candidate has or would tackle them.</p>
  </div>

  <div class="reason reason--2">
    <div class="reason-badge">2</div>
    <h3 class="reason-heading">You describe the job using<br>words, not data.</h3>
    <p class="reason-text">a. Detail oriented means different things to different people. You only find out after you have hired someone that they are not detailed enough (or are too detailed!). The same can happen when we say a candidate needs to be proactive or risk oriented. You only find out later that you hired too much or too little. You used words and not numbers to define what you needed for the role.</p>
  </div>

  <div class="reason reason--3">
    <div class="reason-badge">3</div>
    <h3 class="reason-heading">You assume knowledge<br>and experience equals<br>performance</h3>
    <p class="reason-text">a. Just because someone’s resume says they are a strong manager does not mean they are one. And yet this is how you screen and rank your candidates. The best resumes rise to the top. But resumes are a terrible predictor of performance. Success at one company does not mean success in yours. Who are you overlooking that may be a better performer? (we have an idea below)</p>
  </div>

  <div class="reason reason--4">
    <div class="reason-badge">4</div>
    <h3 class="reason-heading">You are biased and subjective<br>in your assessment of others</h3>
    <p class="reason-text">a. You get attracted to certain resumes and backgrounds. You make judgement calls on phone interviews. You do the same when you meet someone and during an interview. Very few recruitment processes have a way of OBJECTIVELY ranking and comparing candidates. As a result we end up picking someone we like as opposed to someone who will excel in the job.</p>
  </div>

  <div class="reason reason--5">
    <div class="reason-badge">5</div>
    <h3 class="reason-heading">You think your “gut” makes good decisions.</h3>
    <p class="reason-text">a. “Gut” has more to do with how likeable someone is than how effective they will be. Effectiveness comes from a person’s ability to consistently behave in a manner that produces exceptional results. Do not make judgement calls on behaviours a candidate shows but may not be able to consistently repeat.</p>
  </div>

  <div class="brand article-brand"><span class="brand-dot"></span>TALLOWRIDGE</div>
  <div class="site article-site">www.tallowridgeadvisory.com</div>
</section>

</body>
</html>
```